Personal Training

Personal Fitness Trainer
Sports Nutritionist
Individual and Group rates available
Certifications
Global Wellness Coaches Federation
Worldwide Athletic Study Council

Industry/Entity Type

Fitness

Contact Information for Business Card

Dorinda Valcourt
555-284-7160
dvalcourt4@brimfeld.com

```html
<!DOCTYPE html>
<html lang="en">
<head>
<meta charset="utf-8">
<title>Dorinda Valcourt — Business Card</title>
<link rel="stylesheet" href="https://fonts.googleapis.com/css2?family=Tenor+Sans&display=swap">
<style>
  :root {
    --page: #ffffff;
    --teal: #2a7f85;
    --teal-deep: #216d72;
    --teal-light: #3a8f93;
    --grey-tone: #a3a8a5;
    --ink-light: #e9eeee;
    --rule: rgba(255, 255, 255, 0.75);
  }
  * { margin: 0; padding: 0; box-sizing: border-box; }
  html, body {
    width: 1200px;
    height: 849px;
    overflow: hidden;
    background: var(--page);
  }
  .sheet {
    position: relative;
    width: 1200px;
    height: 849px;
  }
  .card {
    position: absolute;
    top: 275px;
    width: 323px;
    height: 183px;
    overflow: hidden;
  }
  .card--front { left: 212px; }
  .card--back {
    left: 684px;
    background: linear-gradient(180deg, var(--teal) 0%, var(--teal-deep) 100%);
  }
  .portrait {
    position: absolute;
    inset: 0;
    background:
      radial-gradient(ellipse 30% 55% at 50% 55%, var(--grey-tone) 0%, rgba(163,168,165,0.55) 55%, rgba(42,127,133,0) 100%),
      radial-gradient(ellipse 22% 40% at 18% 65%, rgba(163,168,165,0.7) 0%, rgba(42,127,133,0) 100%),
      radial-gradient(ellipse 18% 35% at 78% 40%, rgba(163,168,165,0.6) 0%, rgba(42,127,133,0) 100%),
      linear-gradient(180deg, var(--teal-light) 0%, var(--teal) 100%);
  }
  .card-name {
    position: absolute;
    right: 14px;
    bottom: 9px;
    font-family: "Tenor Sans", sans-serif;
    font-size: 10.5px;
    color: var(--ink-light);
  }
  .card-back-art {
    position: absolute;
    inset: 0;
    width: 323px;
    height: 183px;
  }
  .services text {
    font-family: "Tenor Sans", sans-serif;
    fill: var(--ink-light);
  }
  .services .heading { font-size: 9px; letter-spacing: 4.2px; }
  .services .heading--wide { letter-spacing: 9.5px; }
  .services .detail { font-size: 9px; }
  .services .rule { stroke: var(--rule); stroke-width: 0.6; }
  .contact {
    position: absolute;
    right: 16px;
    bottom: 10px;
    font-family: "Tenor Sans", sans-serif;
    font-size: 10px;
    color: var(--ink-light);
    white-space: nowrap;
  }
  .contact .phone { font-size: 11px; letter-spacing: 0.3px; margin-right: 4px; }
</style>
</head>
<body>
  <main class="sheet">
    <section class="card card--front">
      <div class="portrait" role="img" aria-label="Posterized teal and grey photo of the trainer flexing both arms"></div>
      <p class="card-name">Dorinda Valcourt</p>
    </section>

    <section class="card card--back">
      <svg class="card-back-art" viewBox="0 0 323 183" aria-hidden="false">
        <defs>
          <clipPath id="card-edge"><rect width="323" height="183"/></clipPath>
        </defs>
        <g clip-path="url(#card-edge)">
          <g class="services" transform="translate(20 66) rotate(-16)">
            <line class="rule" x1="-60" y1="3" x2="420" y2="3"/>
            <line class="rule" x1="-60" y1="19" x2="420" y2="19"/>
            <line class="rule" x1="-60" y1="34" x2="420" y2="34"/>
            <line class="rule" x1="-60" y1="55" x2="420" y2="55"/>
            <line class="rule" x1="-60" y1="69" x2="420" y2="69"/>
            <line class="rule" x1="-60" y1="84" x2="420" y2="84"/>
            <text class="heading" x="0" y="0">Personal Fitness Trainer</text>
            <text class="heading" x="0" y="16">Sports Nutritionist</text>
            <text class="detail" x="2" y="31">Individual and Group rates available</text>
            <text class="heading heading--wide" x="2" y="52">Certifications</text>
            <text class="detail" x="2" y="66">Global Wellness Coaches Federation</text>
            <text class="detail" x="2" y="81">Worldwide Athletic Study Council</text>
          </g>
        </g>
      </svg>
      <p class="contact"><span class="phone">555-284-7160</span> dvalcourt4@brimfeld.com</p>
    </section>
  </main>
</body>
</html>
```